Business Card Design

I am an Event and Wedding Planner in need of an eye catching business card featuring my logo (attached), my contact details, and my company tagline (Making each one of your gatherings radiant...) I would like the tagline in font similar the logo's font.
Updates
I have just noticed that my logo has a misspelling so for the final design, I will be uploading a corrected logo as soon as I have it.
My apologies.
Reason: Waiting on a corrected logo...Occasions is misspelled and it should say Weddings not Wedding
The logo has been corrected so now Occasions is spelled correctly and it says Weddings instead of Wedding. Please use Edwardian Script ITC as the font for the tagline so it will match the logo. Thank you for your patience.
Target Market(s)
Engaged couples and people hosting milestone celebrations. 25-50 years old, predominately female
Industry/Entity Type
Business
Contact Information for Business Card
Delphine Marsh, Event Manager / Owner, Mobile: 0491 836 254, Email: delphine@radiantgatheringsco.com.au, www.radiantgatheringsco.com.au, Making each one of your gatherings radiant...

```html
<!DOCTYPE html>
<html lang="en">
<head>
<meta charset="utf-8">
<title>Radiant Gatherings Co. — Business Card</title>
<link href="https://fonts.googleapis.com/css2?family=Pinyon+Script&family=EB+Garamond:wght@400&display=swap" rel="stylesheet">
<style>
  :root {
    --page-bg: #ececec;
    --card-bg: #fbfbfa;
    --ink: #2b2b2b;
    --charcoal: #3c3c3e;
    --accent-red: #c8312b;
    --blush: #ecd3c9;
    --blush-soft: #f5e6df;
    --dot: #8a8a8a;
  }
  * { box-sizing: border-box; margin: 0; padding: 0; }
  html, body { width: 1200px; height: 1000px; overflow: hidden; }
  body {
    background: var(--page-bg);
    font-family: "EB Garamond", Georgia, serif;
    color: var(--ink);
    position: relative;
  }
  .card {
    position: absolute;
    left: 320px;
    width: 560px;
    height: 320px;
    background: var(--card-bg);
    box-shadow: 0 10px 24px rgba(0,0,0,0.12);
    overflow: hidden;
  }
  .card::before {
    content: "";
    position: absolute;
    inset: 12px;
    border: 1.5px dotted var(--dot);
    pointer-events: none;
  }
  .card--back { top: 140px; }
  .card--front { top: 530px; }

  /* Back */
  .back-mark {
    position: absolute;
    left: 50%; top: 50%;
    width: 130px; height: 130px;
    margin: -65px 0 0 -65px;
    border-radius: 50%;
    background: var(--charcoal);
    display: flex; align-items: center; justify-content: center;
    text-align: center;
    font-family: "Pinyon Script", cursive;
    font-size: 22px;
    line-height: 1.1;
    color: var(--card-bg);
    padding: 14px;
  }

  /* Front */
  .brand {
    position: absolute;
    left: 30px; top: 30px;
    display: flex; align-items: center; gap: 8px;
  }
  .brand__name {
    font-family: "Pinyon Script", cursive;
    font-size: 22px;
    color: var(--ink);
    line-height: 1;
  }
  .brand__dot {
    width: 10px; height: 10px; border-radius: 50%;
    background: var(--accent-red);
  }
  .heart-decoration {
    position: absolute;
    left: 330px; top: 30px;
    width: 190px; height: 130px;
    background: radial-gradient(ellipse at 50% 50%, var(--blush) 0%, var(--blush-soft) 50%, rgba(245,230,223,0) 70%);
  }
  .tagline {
    position: absolute;
    left: 200px; top: 74px;
    font-family: "Pinyon Script", cursive;
    font-size: 20px;
    line-height: 1.2;
    color: var(--accent-red);
    white-space: nowrap;
  }
  .contact {
    position: absolute;
    left: 250px; top: 168px;
  }
  .contact__name {
    font-family: "Pinyon Script", cursive;
    font-weight: 400;
    font-size: 38px;
    line-height: 1;
    color: var(--ink);
  }
  .contact__role {
    font-size: 16px;
    line-height: 1.2;
    margin: 4px 0 6px;
  }
  .contact__list { list-style: none; font-size: 11px; line-height: 1.45; }
  .contact__list li { display: flex; align-items: center; gap: 6px; }
  .contact__list svg { width: 9px; height: 9px; fill: var(--accent-red); flex: none; }
</style>
</head>
<body>

  <section class="card card--back" aria-label="Card back">
    <div class="back-mark">Radiant Gatherings Co.</div>
  </section>

  <section class="card card--front" aria-label="Card front">
    <div class="brand">
      <span class="brand__name">Radiant Gatherings Co.</span>
      <span class="brand__dot"></span>
    </div>

    <div class="heart-decoration" role="img" aria-label="Large faint blush heart ornament"></div>

    <p class="tagline">Making each one of your gatherings radiant...</p>

    <div class="contact">
      <h1 class="contact__name">Delphine Marsh</h1>
      <p class="contact__role">Event Manager / Owner</p>
      <ul class="contact__list">
        <li>
          <svg viewBox="0 0 10 10" aria-hidden="true"><path d="M2 0.5 L4 2.5 L3 3.8 Q4 6 6.2 7 L7.5 6 L9.5 8 L8 9.5 Q2.5 9 0.5 2 Z"/></svg>
          0491 836 254
        </li>
        <li>
          <svg viewBox="0 0 10 10" aria-hidden="true"><path d="M0 2 H10 V8 H0 Z M0 2 L5 5.5 L10 2" /></svg>
          delphine@radiantgatheringsco.com.au
        </li>
        <li>
          <svg viewBox="0 0 10 10" aria-hidden="true"><circle cx="5" cy="5" r="4.5"/></svg>
          www.radiantgatheringsco.com.au
        </li>
      </ul>
    </div>
  </section>

</body>
</html>
```